Letterhead design for Dental Practice - Ashby Lane Dental Care

Letterhead for Private Dental Practice. To be used for all official correspondance and for printing treatment details on to be given to patients.

Target Market(s)

Private dental patients

Industry/Entity Type

Dental Clinic

Font styles to use
Other font styles liked:
• nexa-light

Colors
33a6d7
1c66ac
85abd2

Requirements
Must have
• info in the footer and header needs to be 3.5cm from upper/lower boader of paper, see photo in uploaded files
• info details:
• tel. 0115 947 3051
• email info@ashbylanedc.co.uk
• ashbylanedentalcare.co.uk
• 17b Ashby Lane West Bridgford Nottingham NG2 7QT
• nexa-light font as in uploaded logo files
Should not have
• No funny tooth pictures

```html
<!DOCTYPE html>
<html lang="en">
<head>
<meta charset="utf-8">
<title>Ashby Lane Dental Care – Letterhead</title>
<link href="https://fonts.googleapis.com/css2?family=Raleway:wght@300;400;600;700&display=swap" rel="stylesheet">
<style>
  :root{
    --sky:#33a6d7;
    --navy:#1c66ac;
    --mist:#85abd2;
    --ink:#3a3a3a;
    --soft-ink:#5c5c5c;
    --paper:#ffffff;
    --backdrop:#e9eaec;
  }
  *{box-sizing:border-box;margin:0;padding:0}
  html,body{width:1200px;height:795px;overflow:hidden;background:var(--backdrop)}
  body{font-family:"Raleway",Arial,sans-serif;color:var(--ink)}
  .letterhead{
    position:absolute;left:333px;top:20px;width:534px;height:755px;
    background:var(--paper);overflow:hidden;
    box-shadow:0 2px 10px rgba(0,0,0,.12);
  }
  .brand{position:absolute;left:40px;top:40px;display:flex;align-items:center;gap:10px}
  .brand__dot{width:26px;height:26px;border-radius:50%;background:var(--sky)}
  .brand__name{font-weight:300;color:var(--sky);font-size:19px;line-height:1.05;letter-spacing:.5px}
  .recipient{position:absolute;left:40px;top:118px;font-size:7.5px;font-weight:700;letter-spacing:.3px}
  .letter-body{position:absolute;left:40px;top:138px;width:330px}
  .letter-body p{font-size:6.6px;line-height:1.45;color:var(--soft-ink);margin-bottom:12px}
  .sign-off{position:absolute;right:44px;top:232px;text-align:left;width:80px}
  .sign-off__name{font-size:7.5px;font-weight:700;letter-spacing:.3px}
  .sign-off__role{font-size:6.6px;color:var(--soft-ink);margin-top:2px}
  .sign-off__signature{display:block;width:70px;height:22px;margin-top:4px;background:linear-gradient(90deg,#dedede,#f1f1f1);border-radius:3px}
  .watermark-ring{position:absolute;left:360px;top:500px;width:110px;height:110px;border-radius:50%;border:1.5px solid rgba(133,171,210,.35)}
  .footer-band{position:absolute;left:0;bottom:0;width:534px;height:200px}
  .contact{position:absolute;left:40px;bottom:48px;font-size:7px;color:var(--ink)}
  .contact__row{display:flex;gap:22px;margin-bottom:6px;align-items:center}
  .contact__item{display:flex;align-items:center;gap:5px;white-space:nowrap}
  .contact__icon{width:10px;height:10px;flex:none}
</style>
</head>
<body>
  <main class="letterhead">
    <header class="brand">
      <span class="brand__dot"></span>
      <span class="brand__name">Ashby Lane<br>Dental Care</span>
    </header>

    <div class="recipient">ELSA MARLOW</div>

    <section class="letter-body">
      <p>Lorem ipsum is simply dummy text of the printing and typesetting industry. Lorem ipsum has been the industry's standard dummy text ever since the 1500s, when an unknown printer took a galley of type and scrambled it to make a type specimen book. It has survived not only five centuries, but also the leap into electronic typesetting, remaining essentially unchanged. It was popularised in the 1960s with the release of Tarnwell sheets containing Lorem ipsum passages, and more recently with desktop publishing software like Quillset Layout including versions of Lorem ipsum.</p>
      <p>Lorem ipsum is simply dummy text of the printing and typesetting industry. Lorem ipsum has been the industry's standard dummy text ever since the 1500s, when an unknown printer took a galley of type and scrambled it to make a type specimen book. It has survived not only five centuries, but also the leap into electronic typesetting, remaining essentially unchanged. It was popularised in the 1960s with the release of Tarnwell sheets containing Lorem ipsum passages, and more recently with desktop publishing software like Quillset Layout including versions of Lorem ipsum. Lorem ipsum has been the industry's standard dummy text ever since the 1500s.</p>
      <p>Lorem ipsum is simply dummy text of the printing and typesetting industry. Lorem ipsum has been the industry's standard dummy text ever since the 1500s, when an unknown printer took a galley of type and scrambled it to make a type specimen book. It has survived not only five centuries, but also the leap into electronic typesetting, remaining essentially unchanged.</p>
      <p>Lorem ipsum is simply dummy text of the printing and typesetting industry. Lorem ipsum has been the industry's standard dummy text ever since the 1500s, when an unknown printer took a galley of type and scrambled it to make a type specimen book.</p>
    </section>

    <aside class="sign-off">
      <div class="sign-off__name">ELSA MARLOW</div>
      <div class="sign-off__role">Owner</div>
      <span class="sign-off__signature" role="img" aria-label="Handwritten signature"></span>
    </aside>

    <div class="watermark-ring"></div>

    <svg class="footer-band" viewBox="0 0 534 200" aria-hidden="true">
      <path d="M0 178 L534 178 L534 186 L0 186 Z" fill="var(--sky)"/>
      <path d="M0 186 L534 186 L534 200 L0 200 Z" fill="var(--navy)"/>
      <path d="M395 170 L395 78 Q395 58 415 58 L534 58 L534 178 L395 178 Z" fill="var(--navy)"/>
      <path d="M0 172 L395 172 L395 176 L0 176 Z" fill="var(--navy)"/>
    </svg>

    <footer class="contact">
      <div class="contact__row">
        <span class="contact__item">
          <svg class="contact__icon" viewBox="0 0 10 10"><circle cx="5" cy="5" r="4.5" fill="none" stroke="var(--navy)"/><path d="M3.3 2.8 L4.3 3.8 L3.8 4.4 Q4.6 5.6 5.6 6.2 L6.2 5.7 L7.2 6.7 L6.6 7.4 Q4.4 7 2.6 3.5 Z" fill="var(--navy)"/></svg>
          0115 947 3051
        </span>
      </div>
      <div class="contact__row">
        <span class="contact__item">
          <svg class="contact__icon" viewBox="0 0 10 10"><circle cx="5" cy="5" r="4.5" fill="none" stroke="var(--navy)"/><rect x="2.6" y="3.3" width="4.8" height="3.4" fill="none" stroke="var(--navy)" stroke-width=".8"/><path d="M2.6 3.3 L5 5.2 L7.4 3.3" fill="none" stroke="var(--navy)" stroke-width=".8"/></svg>
          info@ashbylanedc.co.uk
        </span>
        <span class="contact__item">
          <svg class="contact__icon" viewBox="0 0 10 10"><circle cx="5" cy="5" r="4.5" fill="none" stroke="var(--navy)"/><circle cx="5" cy="5" r="2.3" fill="none" stroke="var(--navy)" stroke-width=".8"/><path d="M2.7 5 H7.3" stroke="var(--navy)" stroke-width=".7"/></svg>
          ashbylanedentalcare.co.uk
        </span>
      </div>
      <div class="contact__row">
        <span class="contact__item">
          <svg class="contact__icon" viewBox="0 0 10 10"><circle cx="5" cy="5" r="4.5" fill="none" stroke="var(--navy)"/><path d="M5 8 Q2.8 5.4 2.8 4.2 A2.2 2.2 0 0 1 7.2 4.2 Q7.2 5.4 5 8 Z" fill="var(--navy)"/><circle cx="5" cy="4.2" r=".8" fill="#fff"/></svg>
          17b Ashby Lane Westbury Marsh Hollingford HF4 7QT
        </span>
      </div>
    </footer>
  </main>
</body>
</html>
```